Postcard Design Harlow Bend D to D

Residential Real Estate, we want to implement a mail campaign in an specific geographic area.We want to include Market information on the area and statistics of the real estate market.This piece is going to be deliver via mail service door to door.

Target Market(s)

Home owners that might be interested in selling their houses

Industry/Entity Type

Real Estate

Font styles to use
Sans Serif

Colors
ec1f27
f78f20

Requirements
Must have
• Attractive look
• Include the information that we just sent to you
• Clear graphics and tables
• Must include clear information about our group

```html
<!DOCTYPE html>
<html lang="en">
<head>
<meta charset="utf-8">
<title>Harlow Bend Market Report Postcard</title>
<link href="https://fonts.googleapis.com/css2?family=Lato:wght@400;700;900&family=Oswald:wght@300;400;600;700&display=swap" rel="stylesheet">
<style>
:root{
  --red:#ec1f27;
  --orange:#f78f20;
  --dark:#2e2b2c;
  --ink:#222;
  --bg:#ece9e4;
  --white:#fff;
  --photo-top:#6f8d4a;
  --photo-mid:#b9ad9a;
  --photo-low:#4f7a32;
  --stamp:#b8b4b5;
}
*{box-sizing:border-box;margin:0;padding:0}
html,body{width:907px;height:1200px;overflow:hidden}
body{background:var(--bg);font-family:'Lato',sans-serif;color:var(--ink);position:relative}
.card{position:absolute;left:95px;width:705px;height:548px;background:var(--white);overflow:hidden;box-shadow:0 2px 6px rgba(0,0,0,.18)}
.card--front{top:50px}
.card--back{top:618px}
.abs{position:absolute}
.shapes{position:absolute;left:0;top:0}

/* front */
.brand{right:28px;top:20px;display:flex;flex-direction:column;align-items:center;gap:6px}
.brand__mark{width:52px;height:52px;background:var(--red)}
.brand__name{font-family:'Lato',sans-serif;font-size:17px;font-weight:400;color:var(--dark);letter-spacing:-.3px}
.headline{right:28px;top:100px;text-align:right;font-family:'Oswald',sans-serif;line-height:1}
.headline__title{font-size:36px;font-weight:700;color:var(--red);letter-spacing:.3px}
.headline__sub{font-size:14.5px;font-weight:600;color:var(--dark);margin-top:6px;letter-spacing:-.2px}
.headline__sub2{font-size:20px;font-weight:300;color:var(--dark);margin-top:3px}
.headline__date{font-size:16px;font-weight:400;color:var(--dark);margin-top:3px;font-family:'Lato',sans-serif}
.greeting{left:345px;top:224px;width:278px;height:38px;background:var(--orange);border-radius:0 20px 20px 0;font-weight:900;font-size:15px;color:var(--dark);padding:11px 0 0 12px;letter-spacing:-.2px}
.facts{left:352px;top:275px;width:328px;list-style:none;font-size:13.4px;line-height:1.28;text-align:justify}
.facts li{position:relative;padding-left:10px;margin-bottom:8px}
.facts li::before{content:"";position:absolute;left:0;top:6px;width:5px;height:5px;border-radius:50%;background:var(--red)}
.quote{left:22px;top:368px;width:270px;font-size:13.4px;line-height:1.3}
.quote__mark{color:var(--red);font-family:'Oswald',sans-serif;font-weight:700;font-size:30px;line-height:0;position:relative;top:10px}
.quote__by{display:block;text-align:right;margin-top:6px;color:var(--red);font-weight:900;font-size:13.5px;padding-right:40px}
.contact-box{left:0;top:453px;width:305px;height:95px;background:var(--dark);border-radius:0 24px 0 0;padding:10px 0 0 45px;color:var(--white)}
.contact-box li{list-style:none;font-size:13.5px;line-height:18px;display:flex;align-items:center;gap:6px}
.contact-box .strong{font-weight:700;font-size:14px}
.ico{width:9px;height:9px;flex:none}

/* back */
.back-panel{left:0;top:0;width:390px;height:548px;background:linear-gradient(180deg,#e8e8e8,#fff 45%,#f1f1f1)}
.back-title{left:0;top:14px;width:380px;text-align:center;font-family:'Oswald',sans-serif;line-height:1.15}
.back-title h2{font-size:18px;font-weight:700;color:var(--red);letter-spacing:.2px}
.back-title p{font-size:12px;font-weight:300;color:var(--dark)}
.section-label{font-weight:900;font-size:10.5px;color:var(--red);text-align:center;line-height:1}
.stats{border-collapse:collapse;table-layout:fixed;font-size:8px;font-weight:700;background:var(--white);line-height:1}
.stats td,.stats th{border:1.3px solid var(--orange);height:15px;padding:0 2px;text-align:left;white-space:nowrap;overflow:hidden}
.stats th{font-size:4.6px;font-weight:700;letter-spacing:-.1px}
.stats th.lead{font-size:8px}
.stats th.tot{font-size:8px;text-align:center}
.stats td.tot{text-align:center}
.stats tr.sum td{font-weight:900}
.stats--b td,.stats--b th{height:14px}
.stamp{left:618px;top:14px;width:58px;height:66px;background:var(--stamp)}
.back-bar{left:0;top:477px;width:448px;height:71px;background:var(--dark);color:var(--white);font-size:13.5px}
.back-bar ul{position:absolute;list-style:none}
.back-bar li{display:flex;align-items:center;gap:6px;line-height:18px}
</style>
</head>
<body>

<section class="card card--front" aria-label="Postcard front">
  <svg class="shapes" width="705" height="548" viewBox="0 0 705 548">
    <path d="M0 0H400C430 70 420 190 340 262C260 330 140 345 0 352V0Z" fill="var(--orange)"/>
    <path d="M0 0H396C420 80 405 200 325 258C250 315 130 330 0 338V0Z" fill="var(--red)"/>
    <path d="M0 0H384C404 85 390 195 315 248C240 302 130 318 0 324V0Z" fill="var(--photo-mid)"/>
  </svg>
  <div class="abs" role="img" aria-label="Photograph of a two-storey family house with porch, trees and flowering garden" style="left:0;top:0;width:400px;height:330px;clip-path:path('M0 0H384C404 85 390 195 315 248C240 302 130 318 0 324Z');background:linear-gradient(180deg,var(--photo-top) 0%,var(--photo-mid) 45%,var(--photo-low) 85%)"></div>

  <div class="abs brand">
    <span class="brand__mark"></span>
    <span class="brand__name">The Morrow Group</span>
  </div>
  <div class="abs headline">
    <div class="headline__title">HARLOW BEND</div>
    <div class="headline__sub">MARKET REPORT OF SINGLE FAMILY SOLD</div>
    <div class="headline__sub2">AND ACTIVE HOMES</div>
    <div class="headline__date">OCTOBER RESULTS 2015</div>
  </div>
  <div class="abs greeting">DEAR HARLOW BEND NEIGHBOR</div>
  <ul class="abs facts">
    <li>We expect that this information will be useful for you to learn about the Real estate market in your neighborhood.</li>
    <li>There are 28 properties “Active for Sale” on the market, with an average price of $303,589 USD and $101.06 USD per sf.</li>
    <li>Average time on market for sale 63 days. In process, “Pending to Close” are 9 houses at average price of $252,808 USD with a sale price of $103.11 per sf. with 34 Days on market.</li>
    <li>The past 6 Months market behavior was as follows: 97 Houses sold at average price of $263,545 with a sale price / sqf. of $100.50</li>
  </ul>
  <p class="abs quote"><span class="quote__mark">“</span> We will be glad to meet with you and have the opportunity to help you with your Real Estate requirements <span class="quote__mark">”</span><span class="quote__by">Elena Morrow</span></p>
  <ul class="abs contact-box">
    <li class="strong"><svg class="ico" viewBox="0 0 10 10"><path d="M2 1l2 2-1 1.5c.6 1.2 1.4 2 2.5 2.5L7 6l2 2-1.5 1.5C4.5 9 1 5.5.5 2.5Z" fill="var(--orange)"/></svg>555-010-2841</li>
    <li class="strong"><svg class="ico" viewBox="0 0 10 10"><rect x="2" y="0.5" width="6" height="9" rx="1" fill="var(--orange)"/></svg>555-010-7736</li>
    <li><svg class="ico" viewBox="0 0 10 10"><circle cx="5" cy="5" r="4.5" fill="var(--orange)"/></svg>themorrowgroup.com</li>
    <li><svg class="ico" viewBox="0 0 10 10"><rect x="0.5" y="2" width="9" height="6.5" fill="var(--orange)"/><path d="M.5 2L5 5.5 9.5 2" stroke="var(--dark)" fill="none"/></svg>elena@elenamorrow.com</li>
  </ul>
</section>

<section class="card card--back" aria-label="Postcard back">
  <div class="abs back-panel"></div>
  <svg class="shapes" width="705" height="548" viewBox="0 0 705 548">
    <path d="M360 0H378C398 150 392 330 345 548H330C370 330 372 150 360 0Z" fill="var(--red)"/>
    <path d="M378 0H392C410 150 400 340 360 548H345C392 330 398 150 378 0Z" fill="var(--orange)"/>
  </svg>
  <div class="abs back-title">
    <h2>UPDATED INFORMATION TO HELP</h2>
    <p>YOU MAKE A SMART DECISION!</p>
  </div>

  <div class="abs section-label" style="left:72px;top:61px;width:258px">DAYS ON MARKET</div>
  <table class="abs stats" style="left:72px;top:80px;width:258px">
    <colgroup><col style="width:54px"><col span="7" style="width:23px"><col style="width:43px"></colgroup>
    <tr><th class="lead">SOLD PRICE</th><th>0-29</th><th>30-59</th><th>60-89</th><th>90-119</th><th>120-149</th><th>150-179</th><th>180-209</th><th class="tot">TOTAL</th></tr>
    <tr><td>$150 -$199</td><td>1</td><td></td><td>1</td><td>1</td><td></td><td></td><td></td><td class="tot">3</td></tr>
    <tr><td>$200 -$249</td><td>2</td><td></td><td></td><td>1</td><td>1</td><td></td><td></td><td class="tot">4</td></tr>
    <tr><td>$250 -$299</td><td>1</td><td>3</td><td></td><td>2</td><td></td><td></td><td></td><td class="tot">6</td></tr>
    <tr><td>$300 -$ 349</td><td>5</td><td>2</td><td></td><td></td><td></td><td></td><td>2</td><td class="tot">9</td></tr>
    <tr><td>$350 -$399</td><td>2</td><td></td><td></td><td>1</td><td></td><td>1</td><td></td><td class="tot">4</td></tr>
    <tr><td>$400 -$449</td><td>1</td><td></td><td></td><td></td><td></td><td></td><td></td><td class="tot">1</td></tr>
    <tr><td>$450 -$499</td><td></td><td></td><td></td><td>1</td><td></td><td></td><td></td><td class="tot">28</td></tr>
    <tr class="sum"><td>TOTAL</td><td>12</td><td>5</td><td>1</td><td>6</td><td>1</td><td>1</td><td>2</td><td class="tot">97</td></tr>
  </table>

  <div class="abs section-label" style="left:60px;top:234px;width:258px;font-size:9.5px">THE HISTORIC PRICE PER SQF. 2003 - 2014</div>
  <svg class="abs" style="left:108px;top:250px" width="166" height="92" viewBox="0 0 166 92" role="img" aria-label="Bar chart of price per square foot 2003 to 2014">
    <g font-family="Lato, sans-serif" font-size="4" fill="#666">
      <text x="0" y="7">100</text><text x="2" y="24">90</text><text x="2" y="41">80</text><text x="2" y="58">70</text><text x="2" y="75">60</text>
    </g>
    <g stroke="#e6e6e6" stroke-width=".5"><line x1="12" y1="5" x2="164" y2="5"/><line x1="12" y1="22" x2="164" y2="22"/><line x1="12" y1="39" x2="164" y2="39"/><line x1="12" y1="56" x2="164" y2="56"/></g>
    <line x1="12" y1="73" x2="164" y2="73" stroke="#999" stroke-width=".6"/>
    <g fill="var(--orange)">
      <rect x="14" y="56" width="8" height="17"/><rect x="26.5" y="63" width="8" height="10"/><rect x="39" y="56" width="8" height="17"/><rect x="51.5" y="48" width="8" height="25"/>
      <rect x="64" y="32" width="8" height="41"/><rect x="76.5" y="42" width="8" height="31"/><rect x="89" y="34" width="8" height="39"/><rect x="101.5" y="33" width="8" height="40"/>
      <rect x="114" y="34" width="8" height="39"/><rect x="126.5" y="29" width="8" height="44"/><rect x="139" y="22" width="8" height="51"/><rect x="151.5" y="10" width="8" height="63"/>
    </g>
    <g font-family="Lato, sans-serif" font-size="3.6" fill="#666">
      <text x="14" y="79">2003</text><text x="26.5" y="79">2004</text><text x="39" y="79">2005</text><text x="51.5" y="79">2006</text><text x="64" y="79">2007</text><text x="76.5" y="79">2008</text>
      <text x="89" y="79">2009</text><text x="101.5" y="79">2010</text><text x="114" y="79">2011</text><text x="126.5" y="79">2012</text><text x="139" y="79">2013</text><text x="151.5" y="79">2014</text>
    </g>
  </svg>

  <div class="abs section-label" style="left:55px;top:345px;width:273px">DAYS ON MARKET</div>
  <table class="abs stats stats--b" style="left:55px;top:358px;width:273px">
    <colgroup><col style="width:49px"><col span="8" style="width:23px"><col style="width:40px"></colgroup>
    <tr><th class="lead">SOLD PRICE</th><th>0-29</th><th>30-59</th><th>60-89</th><th>90-119</th><th>120-149</th><th>150-179</th><th>180-209</th><th>210-239</th><th class="tot">TOTAL</th></tr>
    <tr><td>$170 -$219</td><td>23</td><td>3</td><td>3</td><td>1</td><td>2</td><td>1</td><td></td><td></td><td class="tot">33</td></tr>
    <tr><td>$220 -$ 269</td><td>11</td><td>5</td><td>5</td><td>1</td><td></td><td></td><td></td><td></td><td class="tot">22</td></tr>
    <tr><td>$270 -$319</td><td>10</td><td>5</td><td>5</td><td>1</td><td></td><td></td><td></td><td></td><td class="tot">21</td></tr>
    <tr><td>$320 -$369</td><td>9</td><td></td><td></td><td></td><td></td><td></td><td>1</td><td>2</td><td class="tot">13</td></tr>
    <tr><td>$370 -$ 420</td><td>3</td><td>3</td><td>3</td><td></td><td></td><td></td><td></td><td></td><td class="tot">8</td></tr>
    <tr class="sum"><td>TOTAL</td><td>56</td><td>16</td><td>14</td><td>3</td><td>3</td><td>2</td><td>1</td><td>2</td><td class="tot">97</td></tr>
  </table>

  <div class="abs stamp" aria-label="Stamp area"></div>

  <div class="abs back-bar">
    <ul style="left:40px;top:17px">
      <li><svg class="ico" viewBox="0 0 10 10"><path d="M2 1l2 2-1 1.5c.6 1.2 1.4 2 2.5 2.5L7 6l2 2-1.5 1.5C4.5 9 1 5.5.5 2.5Z" fill="var(--orange)"/></svg>555-010-2841</li>
      <li><svg class="ico" viewBox="0 0 10 10"><rect x="2" y="0.5" width="6" height="9" rx="1" fill="var(--orange)"/></svg>555-010-7736</li>
    </ul>
    <ul style="left:228px;top:12px">
      <li><svg class="ico" viewBox="0 0 10 10"><circle cx="5" cy="5" r="4.5" fill="var(--orange)"/></svg>themorrowgroup.com</li>
      <li><svg class="ico" viewBox="0 0 10 10"><rect x="0.5" y="2" width="9" height="6.5" fill="var(--orange)"/><path d="M.5 2L5 5.5 9.5 2" stroke="var(--dark)" fill="none"/></svg>elena@elenamorrow.com</li>
    </ul>
  </div>
</section>

</body>
</html>
```